General pharmacy flyer for a pharmacy. see attached files for similar flyer design
picture should be of a black person/pharmacist
Services available
Repeat Prescription collection
Emergency Contraception
Contraceptive pill
Vitamins
and more.....
Pharmacy

```html
<!DOCTYPE html>
<html lang="en">
<head>
<meta charset="utf-8">
<title>Ivy Pharmacy Flyer</title>
<link href="https://fonts.googleapis.com/css2?family=Montserrat:wght@400;500;700&family=Cormorant+Garamond:ital,wght@1,600&family=Titillium+Web:ital,wght@1,300&display=swap" rel="stylesheet">
<style>
  :root {
    --stage: #e9731b;
    --blue: #1b74c7;
    --green: #3bb54a;
    --green-deep: #2fa03f;
    --navy: #1e1a4a;
    --yellow: #ffd51f;
    --white: #ffffff;
    --grey: #dfe1e4;
  }
  * { margin: 0; padding: 0; box-sizing: border-box; }
  html, body { width: 1200px; height: 900px; overflow: hidden; background: var(--stage); }
  .flyer {
    position: absolute; left: 273px; top: 21px;
    width: 743px; height: 975px;
    transform: scale(0.88); transform-origin: 0 0;
    font-family: "Montserrat", sans-serif; color: var(--white);
    overflow: hidden;
    box-shadow: 0 18px 30px rgba(0,0,0,0.35);
  }
  .flyer-shapes { position: absolute; inset: 0; }
  .abs { position: absolute; }
  .slogan-art { left: 35px; top: 35px; width: 165px; height: 170px; border-radius: 50%; background: rgba(255,213,31,0.18); }
  .rule { height: 2px; background: var(--white); }
  .headline { left: 38px; top: 310px; font-weight: 700; font-size: 27px; line-height: 32.5px; letter-spacing: 0.5px; white-space: nowrap; }
  .services-title { left: 34px; top: 552px; font-family: "Cormorant Garamond", serif; font-style: italic; font-weight: 600; font-size: 46px; }
  .services { left: 32px; top: 616px; list-style: none; font-size: 25px; line-height: 30.5px; }
  .services li { position: relative; padding-left: 24px; }
  .services li::before { content: ""; position: absolute; left: 0; top: 11px; width: 11px; height: 11px; border: 2px solid var(--yellow); border-radius: 50%; }
  .brand-dot { left: 262px; top: 32px; width: 80px; height: 80px; border-radius: 50%; background: var(--green); }
  .brand-name { left: 366px; top: 52px; font-weight: 700; font-size: 40px; line-height: 44px; color: var(--navy); letter-spacing: -0.5px; white-space: nowrap; }
  .brand-tagline { left: 364px; top: 104px; font-family: "Titillium Web", sans-serif; font-style: italic; font-weight: 300; font-size: 20px; line-height: 26px; color: var(--green); white-space: nowrap; }
  .contact { left: 398px; top: 698px; list-style: none; font-size: 17px; line-height: 21px; }
  .contact li { display: flex; gap: 10px; align-items: flex-start; margin-bottom: 20px; white-space: nowrap; }
  .contact svg { flex: none; width: 22px; height: 24px; }
  .hours-band { left: 0; top: 883px; width: 440px; height: 54px; background: var(--green); }
  .hours-label { left: 28px; top: 886px; font-weight: 700; font-size: 21px; line-height: 22px; text-align: center; }
  .hours-clock { left: 134px; top: 893px; width: 36px; height: 36px; }
  .hours-times { left: 190px; top: 895px; font-size: 14px; line-height: 17px; white-space: nowrap; }
</style>
</head>
<body>
<div class="flyer">
  <svg class="flyer-shapes" width="743" height="975" viewBox="0 0 743 975">
    <defs>
      <linearGradient id="photoTone" x1="0" y1="0" x2="1" y2="1">
        <stop offset="0" stop-color="#d9dde2"/>
        <stop offset="0.55" stop-color="#f1ece9"/>
        <stop offset="1" stop-color="#c9a08a"/>
      </linearGradient>
    </defs>
    <rect width="743" height="975" fill="var(--blue)"/>
    <polygon points="198,0 250,0 290,180 243,180" fill="var(--grey)"/>
    <polygon points="250,0 743,0 743,180 290,180" fill="var(--white)"/>
    <polygon points="243,180 743,180 743,670 364,670" fill="url(#photoTone)" role="img" aria-label="Smiling pharmacist in a white coat standing in front of pharmacy shelves"/>
    <polygon points="364,670 743,670 743,975 440,975" fill="var(--green)"/>
    <polygon points="364,670 420,670 490,975 440,975" fill="var(--green-deep)"/>
  </svg>

  <div class="abs slogan-art" role="img" aria-label="Hand-lettered slogan: We care about your Health"></div>

  <span class="abs brand-dot"></span>
  <p class="abs brand-name">IVY PHARMACY</p>
  <p class="abs brand-tagline">We Care About Your Health</p>

  <div class="abs rule" style="left:37px;top:285px;width:211px"></div>
  <h1 class="abs headline">COME VISIT<br>IVY PHARMACY<br>FOR ALL YOUR<br>PRESCRIPTION<br>NEEDS AND MORE</h1>
  <div class="abs rule" style="left:37px;top:505px;width:260px"></div>

  <h2 class="abs services-title">Services include</h2>
  <ul class="abs services">
    <li>Repeat prescription<br>collection</li>
    <li>Emergency<br>contraception</li>
    <li>Contraceptive pill</li>
    <li>Vitamins</li>
    <li>And More................</li>
  </ul>

  <ul class="abs contact">
    <li>
      <svg viewBox="0 0 22 24"><path d="M11 1a8 8 0 0 0-8 8c0 6 8 14 8 14s8-8 8-14a8 8 0 0 0-8-8zm0 11a3 3 0 1 1 0-6 3 3 0 0 1 0 6z" fill="var(--yellow)"/></svg>
      <span>27 Harbor Road (Corner of Harbor<br>and Mill Street)</span>
    </li>
    <li style="margin-left:12px">
      <svg viewBox="0 0 22 24"><path d="M11 1a8 8 0 0 0-8 8c0 6 8 14 8 14s8-8 8-14a8 8 0 0 0-8-8zm0 11a3 3 0 1 1 0-6 3 3 0 0 1 0 6z" fill="var(--yellow)"/></svg>
      <span>Bay Quarter, Westhaven</span>
    </li>
    <li style="margin-left:24px">
      <svg viewBox="0 0 22 24"><path d="M5 2l4 1 1 5-3 2c1 3 3 5 6 7l2-3 5 1 1 4c-1 2-3 3-5 3C9 21 2 13 2 6c0-2 1-3 3-4z" fill="var(--yellow)"/></svg>
      <span>555 0142 &amp; 555 0178</span>
    </li>
    <li style="margin-left:36px">
      <svg viewBox="0 0 22 24"><rect x="1" y="6" width="20" height="14" fill="none" stroke="var(--yellow)" stroke-width="2"/><path d="M1 6l10 8 10-8" fill="none" stroke="var(--yellow)" stroke-width="2"/></svg>
      <span>ivypharmacy@example.com</span>
    </li>
  </ul>

  <div class="abs hours-band"></div>
  <p class="abs hours-label">Opening<br>hours</p>
  <svg class="abs hours-clock" viewBox="0 0 36 36"><circle cx="18" cy="18" r="15.5" fill="none" stroke="var(--white)" stroke-width="3"/><path d="M18 9v10h8" fill="none" stroke="var(--white)" stroke-width="3"/></svg>
  <p class="abs hours-times">Monday - Fridays - 9am -6pm<br>Saturdays 10am - 5pm</p>
</div>
</body>
</html>
```